Art Wall - Illustrates "Be Colorful"

I have a seasonal color business called Willow Gate Blooms. We plant containers and add colorful annuals to garden beds. I need a 6' tall by 18' long banner that will be hung on a wall or possibly used on the side of my enclosed trailer. The banner will be used as backdrop for ladies taking pictures together and as a backdrop for colorful container gardens to be photographed for our website. It should have the words "Be Colorful" on it. I would like for it to look like a fun art wall that you would take a picture in front of in a downtown area. The art should work well with our logo. We love flowers but other ideas are welcome. Feel free to look at our instagram @willowgatebloomsokc to see examples of our work. I have uploaded our logo and a colorful flower picture we liked (great colors) but didn't quite work with our logo and a fun colorful wall at a restaurant that we really like.

Target Market(s)

women ages 30-45, wealthy, like to feel like they are trendy

Industry/Entity Type

Landscape Gardening

Font styles to use
Serif

Requirements
Must have
• The words "Be Colorful" on it and some space that would good for people to stand or objects to be placed to be photographed.
Nice to have
• We really like the colors in the "sun and skip" t-shirt picture I have attached. Also like the watercolor, alcohol ink, or hand-painted look.
Should not have
• Please do not include our logo on the banner. It will be added as a watermark to our photos.

Please do not literally use the logo flower in the design. Feel free to use pieces or inspiration from the logo but the wall should look more like art and less like a cartoon.

```html
<!DOCTYPE html>
<html lang="en">
<head>
<meta charset="utf-8">
<title>Be Colorful – Art Wall Options</title>
<link href="https://fonts.googleapis.com/css2?family=Dancing+Script:wght@600&display=swap" rel="stylesheet">
<style>
  :root {
    --page: #ffffff;
    --ink-olive: #5b5441;
    --ink-bronze-a: #8d5e2c;
    --ink-bronze-b: #3e2a14;
    --ink-blue: #2c5b97;
  }
  html, body {
    margin: 0;
    padding: 0;
    overflow: hidden;
    background: var(--page);
  }
  .canvas {
    position: relative;
    width: 848px;
    height: 1200px;
    background: var(--page);
    overflow: hidden;
  }
  .wall-option {
    position: absolute;
    left: 0;
    width: 834px;
    height: 276px;
  }
  .wall-option--blush { top: 97px; }
  .wall-option--meadow { top: 459px; }
  .wall-option--lagoon { top: 805px; }
  .ink-wash {
    position: absolute;
    inset: 0;
    width: 100%;
    height: 100%;
  }
  .headline {
    position: absolute;
    left: 164px;
    top: 41px;
    margin: 0;
    padding: 0 24px 8px 10px;
    font-family: "Dancing Script", cursive;
    font-weight: 600;
    font-size: 112px;
    line-height: 1.3;
    letter-spacing: 1px;
    white-space: nowrap;
  }
  .headline--olive { color: var(--ink-olive); }
  .headline--bronze {
    background: linear-gradient(90deg, var(--ink-bronze-a), var(--ink-bronze-b));
    -webkit-background-clip: text;
    background-clip: text;
    -webkit-text-fill-color: transparent;
    color: transparent;
  }
  .headline--blue { color: var(--ink-blue); }
</style>
</head>
<body>
<main class="canvas">

  <section class="wall-option wall-option--blush">
    <svg class="ink-wash" viewBox="0 0 834 276" preserveAspectRatio="none" role="img" aria-label="Alcohol ink artwork in blush pink, soft grey and dusty blue with gold veins and gold flecks">
      <defs>
        <linearGradient id="wash-blush" x1="0" y1="0" x2="1" y2="0">
          <stop offset="0" stop-color="#f3cbc4"/>
          <stop offset="0.3" stop-color="#f1cdc6"/>
          <stop offset="0.42" stop-color="#dcd9da"/>
          <stop offset="0.6" stop-color="#a9b5c7"/>
          <stop offset="1" stop-color="#b4c0d0"/>
        </linearGradient>
        <linearGradient id="fade-blush" x1="0" y1="0" x2="0" y2="1">
          <stop offset="0.6" stop-color="#fff" stop-opacity="0"/>
          <stop offset="1" stop-color="#fff" stop-opacity="0.75"/>
        </linearGradient>
      </defs>
      <path d="M0 0 H834 V272 C720 274 640 262 580 240 C500 214 430 250 340 240 C260 232 230 172 130 182 C70 188 25 228 0 252 Z" fill="url(#wash-blush)"/>
      <path d="M0 0 H834 V272 C720 274 640 262 580 240 C500 214 430 250 340 240 C260 232 230 172 130 182 C70 188 25 228 0 252 Z" fill="url(#fade-blush)"/>
    </svg>
    <h1 class="headline headline--olive">Be Colorful</h1>
  </section>

  <section class="wall-option wall-option--meadow">
    <svg class="ink-wash" viewBox="0 0 834 276" preserveAspectRatio="none" role="img" aria-label="Alcohol ink artwork in fresh green, soft grey and plum mauve with turquoise veins and flecks">
      <defs>
        <linearGradient id="wash-meadow" x1="0" y1="0" x2="1" y2="0">
          <stop offset="0" stop-color="#aef0b4"/>
          <stop offset="0.3" stop-color="#b6efbb"/>
          <stop offset="0.42" stop-color="#dcdcdc"/>
          <stop offset="0.6" stop-color="#c99ab6"/>
          <stop offset="1" stop-color="#d3aec3"/>
        </linearGradient>
        <linearGradient id="fade-meadow" x1="0" y1="0" x2="0" y2="1">
          <stop offset="0.6" stop-color="#fff" stop-opacity="0"/>
          <stop offset="1" stop-color="#fff" stop-opacity="0.75"/>
        </linearGradient>
      </defs>
      <path d="M0 0 H834 V272 C720 274 640 262 580 240 C500 214 430 250 340 240 C260 232 230 172 130 182 C70 188 25 228 0 252 Z" fill="url(#wash-meadow)"/>
      <path d="M0 0 H834 V272 C720 274 640 262 580 240 C500 214 430 250 340 240 C260 232 230 172 130 182 C70 188 25 228 0 252 Z" fill="url(#fade-meadow)"/>
    </svg>
    <h1 class="headline headline--bronze">Be Colorful</h1>
  </section>

  <section class="wall-option wall-option--lagoon">
    <svg class="ink-wash" viewBox="0 0 834 276" preserveAspectRatio="none" role="img" aria-label="Alcohol ink artwork in aqua, soft grey and warm sand brown with blue veins and flecks">
      <defs>
        <linearGradient id="wash-lagoon" x1="0" y1="0" x2="1" y2="0">
          <stop offset="0" stop-color="#a6ecf0"/>
          <stop offset="0.3" stop-color="#b4eef0"/>
          <stop offset="0.42" stop-color="#dddcdc"/>
          <stop offset="0.6" stop-color="#c7a888"/>
          <stop offset="1" stop-color="#d4b99e"/>
        </linearGradient>
        <linearGradient id="fade-lagoon" x1="0" y1="0" x2="0" y2="1">
          <stop offset="0.6" stop-color="#fff" stop-opacity="0"/>
          <stop offset="1" stop-color="#fff" stop-opacity="0.75"/>
        </linearGradient>
      </defs>
      <path d="M0 0 H834 V272 C720 274 640 262 580 240 C500 214 430 250 340 240 C260 232 230 172 130 182 C70 188 25 228 0 252 Z" fill="url(#wash-lagoon)"/>
      <path d="M0 0 H834 V272 C720 274 640 262 580 240 C500 214 430 250 340 240 C260 232 230 172 130 182 C70 188 25 228 0 252 Z" fill="url(#fade-lagoon)"/>
    </svg>
    <h1 class="headline headline--blue">Be Colorful</h1>
  </section>

</main>
</body>
</html>
```